Real Estate Brokerage Stationery Designs

I am looking to have presentation folders with business card slots on both sides along with pockets on both sides. I've attached logos, website colors along with current business card designs.

I am looking for envelope designs both big and small. Possibly new business card designs, notepad templates for big and small notepads. Letterhead designs. Pop socket designs. Realtors name badge designs.

www.brightkeelhomes.example

```html
<!DOCTYPE html>
<html lang="en">
<head>
<meta charset="utf-8">
<title>Brightkeel Homes – Presentation Folder</title>
<link href="https://fonts.googleapis.com/css2?family=Open+Sans:wght@400;600;700&family=Oswald:wght@500&display=swap" rel="stylesheet">
<style>
  :root{
    --bg:#cfe4f8;
    --blue:#2f7fd3;
    --blue-light:#4f97df;
    --blue-deep:#1457a8;
    --navy:#0b2f66;
    --pocket:#4a8ed6;
    --paper:#f4f4f4;
    --paper-shade:#dedede;
    --ghost:#a9a9a9;
    --ink:#222;
    --white:#fff;
    --grey-text:#7a7a7a;
  }
  *{box-sizing:border-box;margin:0;padding:0}
  html,body{width:1200px;height:1080px;overflow:hidden}
  body{background:var(--bg);font-family:"Open Sans",sans-serif;position:relative}

  .spread{position:absolute;left:240px;width:720px;height:480px;display:flex;box-shadow:0 10px 30px rgba(20,60,120,.25)}
  .spread--outside{top:20px}
  .spread--inside{top:560px}
  .panel{position:relative;width:360px;height:480px;overflow:hidden}

  /* outside */
  .panel--cover{background:linear-gradient(160deg,var(--blue-light),var(--blue) 55%,var(--blue-deep))}
  .band{position:absolute;left:0;right:0;top:125px;height:200px;background:var(--blue-deep)}
  .photo{position:absolute;left:0;right:0;top:140px;height:170px}
  .photo--towers{background:linear-gradient(180deg,#9cc3e6 0%,#c9d8d6 45%,#5f8a55 100%)}
  .photo--house{background:linear-gradient(180deg,#6f8fb6 0%,#c7b79b 55%,#5a5145 100%)}
  .seal{position:absolute;left:80px;top:125px;width:200px;height:200px;border-radius:50%;
        background:radial-gradient(circle,#fff 40%,#dcdcdc);border:7px solid var(--blue-deep);
        display:flex;align-items:center;justify-content:center}
  .brand{font-weight:700;color:var(--ink);font-size:22px;text-align:center;line-height:1.15}
  .web{position:absolute;left:0;right:0;bottom:38px;text-align:center;color:var(--white);font-weight:700;font-size:14px;letter-spacing:.2px}

  .contacts{position:absolute;left:0;right:0;top:345px;display:flex;justify-content:space-between;padding:0 8px}
  .contact{text-align:center;color:var(--white);font-size:8px;font-weight:600;line-height:1.45;white-space:nowrap}
  .contact--mail{width:140px}
  .contact--phone{width:80px}
  .contact--address{width:110px}
  .contact svg{display:block;margin:0 auto 6px;width:22px;height:22px}
  .services{position:absolute;left:0;right:0;top:432px;height:30px;background:var(--white);
            display:flex;align-items:center;justify-content:center;gap:6px;font-size:7.5px;font-weight:600;color:var(--grey-text);white-space:nowrap}
  .services span+span{border-left:1px solid var(--grey-text);padding-left:6px}
  .services-tab{position:absolute;left:140px;top:420px;width:80px;height:12px;border-radius:6px 6px 0 0;
                background:var(--blue-deep);color:var(--white);font-size:6.5px;font-weight:700;text-align:center;line-height:12px;letter-spacing:.5px}

  /* inside */
  .panel--left{background:linear-gradient(90deg,var(--paper),#e6e6e6)}
  .panel--right{background:linear-gradient(90deg,var(--paper-shade),#cfcfcf)}
  .ghost-brand{position:absolute;left:0;right:0;top:150px;text-align:center;color:var(--ghost);font-weight:700;font-size:30px;line-height:1.1}
  .ghost-brand small{display:block;font-size:15px;letter-spacing:2px;margin-top:4px}
  .pocket{position:absolute;left:0;right:0;bottom:0;height:175px;background:var(--pocket);border-top:2px solid #3b7ec6}
  .card{position:absolute;left:75px;top:25px;width:200px;height:110px;background:var(--white);display:flex;box-shadow:0 2px 4px rgba(0,0,0,.2)}
  .card-info{flex:1;padding:14px 6px 6px 10px;display:flex;flex-direction:column}
  .card-brand{font-weight:700;font-size:12px;color:var(--blue-deep)}
  .card-lines{font-size:5.5px;color:#444;margin-top:auto;line-height:1.35;white-space:nowrap}
  .badges{display:flex;gap:3px;margin-top:5px}
  .badges i{display:block;width:12px;height:9px;background:#333}
  .card-photo{position:relative;width:78px;background:linear-gradient(180deg,#e9e9e9,#bcbcbc)}
  .card-name{position:absolute;left:-14px;right:0;bottom:8px;background:#111;color:var(--white);font-family:"Oswald",sans-serif;font-size:8px;padding:3px 4px;text-transform:uppercase;white-space:nowrap}
  .card-name b{color:#4aa3ff;font-weight:500}
  .card-name small{display:block;font-size:5px;text-align:right;color:#ccc}
</style>
</head>
<body>

<section class="spread spread--outside" aria-label="Folder outside">
  <div class="panel panel--cover panel--back">
    <div class="band"></div>
    <div class="photo photo--house" role="img" aria-label="Photo of a lit two-storey family home at dusk"></div>
    <div class="contacts">
      <div class="contact contact--mail">
        <svg viewBox="0 0 22 22"><circle cx="11" cy="11" r="11" fill="#0b2f66"/><circle cx="12" cy="10" r="4" fill="none" stroke="#fff" stroke-width="1.6"/><line x1="9" y1="13" x2="6" y2="16" stroke="#fff" stroke-width="1.8"/></svg>
        hello@brightkeelhomes.example<br>www.brightkeelhomes.example
      </div>
      <div class="contact contact--phone">
        <svg viewBox="0 0 22 22"><circle cx="11" cy="11" r="11" fill="#0b2f66"/><circle cx="11" cy="9" r="3" fill="#fff"/><path d="M5 16c1-3 11-3 12 0z" fill="#fff"/></svg>
        555-010-2471<br>555-010-3386
      </div>
      <div class="contact contact--address">
        <svg viewBox="0 0 22 22"><circle cx="11" cy="11" r="11" fill="#0b2f66"/><path d="M5 11l6-5 6 5h-2v5h-8v-5z" fill="#fff"/></svg>
        740 Harbor Row, Ste 12,<br>Coral Bay, FL 30010
      </div>
    </div>
    <div class="services-tab">SERVICES</div>
    <div class="services">
      <span>Residential Real Estate</span><span>Commercial Real Estate</span><span>Property Management</span><span>Investments</span>
    </div>
  </div>
  <div class="panel panel--cover panel--front">
    <div class="band"></div>
    <div class="photo photo--towers" role="img" aria-label="Photo of waterfront condominium towers among palm trees"></div>
    <div class="seal"><p class="brand">Brightkeel<br>Homes</p></div>
    <p class="web">www.brightkeelhomes.example</p>
  </div>
</section>

<section class="spread spread--inside" aria-label="Folder inside">
  <div class="panel panel--left">
    <p class="ghost-brand">Brightkeel Homes<small>REALTY</small></p>
    <div class="pocket">
      <div class="card">
        <div class="card-info">
          <p class="card-brand">Brightkeel Homes</p>
          <p class="card-lines">Residential Real Estate |<br>Commercial Real Estate<br>Property Management | Investments</p>
          <div class="badges"><i></i><i></i><i></i></div>
        </div>
        <div class="card-photo" role="img" aria-label="Portrait photo of the broker">
          <p class="card-name">Marcus <b>Hale</b><small>BROKER</small></p>
        </div>
      </div>
    </div>
  </div>
  <div class="panel panel--right">
    <p class="ghost-brand">Brightkeel Homes<small>REALTY</small></p>
    <div class="pocket">
      <div class="card">
        <div class="card-info">
          <p class="card-brand">Brightkeel Homes</p>
          <p class="card-lines">Residential Real Estate |<br>Commercial Real Estate<br>Property Management | Investments</p>
          <div class="badges"><i></i><i></i><i></i></div>
        </div>
        <div class="card-photo" role="img" aria-label="Portrait photo of the realtor">
          <p class="card-name">Tobin <b>Castell</b><small>REALTOR</small></p>
        </div>
      </div>
    </div>
  </div>
</section>

</body>
</html>
```